Unique Flyer Project - www.plumvaleforms.com.au

The purpose of this flyer is trying to get recipients to visit the website www.plumvaleforms.com.au and sign up to the offer. I need it to be simple/to the point, eye catching and professional. I will post up a basic idea I have but feel free to put your own spin on it if you think you have great ideas to get people to visit the site, if not then just improve upon the quality of mine and make it look like a respected company.

I also think a red band or something that REALLY catches the eye highlighting one of the important aspects of the flyer (the domain?) could be great so even if someone is about to put it in the bin, the popping red-on-white-background catches their eye so they end up looking at and reading the flyer.

I would also love a VERY SIMPLE design for the backside of the flyer, just a red box/band (whatever you think is good) with the domain 'www.plumvaleforms.com.au' in it. NOTHING ELSE! Just so if it's floating around the table and it's upside down, there's something eye catching that might entice the householder to look at it.

DESIGN IS FOR DL FLYER: 99mm X 210mm

Target Market(s)

Australian Residents interested in earning money from home.

Industry/Entity Type

It Company

Requirements
Must have
• Eye catching (mainly red band/box/bar on front & back page), SIMPLE, elegant/professional.
Should not have
• ANYTHING unnecessary to the reader that will distract them from the ultimate point - GET PAID TO DO SURVEYS FROM YOUR OWN HOME ON THE COMPUTER!

```html
<!DOCTYPE html>
<html lang="en">
<head>
<meta charset="utf-8">
<title>Plumvale Forms – DL Flyer, Front and Back</title>
<link rel="stylesheet" href="https://fonts.googleapis.com/css2?family=Anton&display=swap">
<style>
  :root {
    --stage: #3a3a3a;
    --paper: #ffffff;
    --brand-red: #d2232a;
    --ink: #111111;
    --on-red: #ffffff;
    --flyer-w: 302px;
    --flyer-h: 640px;
  }

  * { box-sizing: border-box; margin: 0; padding: 0; }

  html, body {
    width: 1200px;
    height: 750px;
    overflow: hidden;
  }

  body {
    background: var(--stage);
    font-family: "Anton", "Arial Narrow", sans-serif;
    display: flex;
    align-items: center;
    justify-content: center;
    gap: 56px;
  }

  .flyer {
    width: var(--flyer-w);
    height: var(--flyer-h);
    position: relative;
    overflow: hidden;
    box-shadow: 0 10px 30px rgba(0, 0, 0, 0.35);
  }

  /* Front side */
  .flyer--front {
    background: var(--paper);
    display: flex;
    flex-direction: column;
  }

  .front__headline-area {
    padding: 34px 22px 16px 24px;
  }

  .headline {
    color: var(--ink);
    font-size: 68px;
    line-height: 0.9;
    text-transform: uppercase;
    letter-spacing: 0.5px;
  }

  .headline__line { display: block; }
  .headline__line--accent { color: var(--brand-red); }

  .subline {
    margin-top: 10px;
    color: var(--brand-red);
    font-size: 12.5px;
    letter-spacing: 0.3px;
    text-transform: uppercase;
    white-space: nowrap;
  }

  .front__red-band {
    flex: 1;
    background: var(--brand-red);
    position: relative;
    padding: 16px 22px 0 24px;
  }

  .web-address {
    color: var(--on-red);
    font-size: 21px;
    letter-spacing: 0.2px;
    white-space: nowrap;
  }

  .front__illustration {
    position: absolute;
    left: 50%;
    bottom: 0;
    transform: translateX(-50%);
    width: 190px;
    height: 170px;
    display: block;
  }

  /* Back side */
  .flyer--back {
    background: var(--brand-red);
  }

  .back__web-address {
    position: absolute;
    left: 58px;
    bottom: 36px;
    transform-origin: left bottom;
    transform: rotate(-90deg) translateY(100%);
    color: var(--on-red);
    font-size: 32px;
    letter-spacing: 0.3px;
    white-space: nowrap;
  }
</style>
</head>
<body>

  <article class="flyer flyer--front" aria-label="Flyer front">
    <header class="front__headline-area">
      <h1 class="headline">
        <span class="headline__line">Get</span>
        <span class="headline__line headline__line--accent">Paid</span>
        <span class="headline__line">To Do</span>
        <span class="headline__line">Surveys</span>
      </h1>
      <p class="subline">From your own home on the computer!</p>
    </header>

    <section class="front__red-band">
      <p class="web-address">www.plumvaleforms.com.au</p>
      <svg class="front__illustration" viewBox="0 0 190 170" role="img"
           aria-label="Silhouette of a person relaxing in a chair at a desk with a laptop and a cup">
        <defs>
          <linearGradient id="silhouette-tone" x1="0" y1="0" x2="0" y2="1">
            <stop offset="0" stop-color="#1a1a1a" stop-opacity="0.55"/>
            <stop offset="1" stop-color="#111111" stop-opacity="0.9"/>
          </linearGradient>
        </defs>
        <rect x="0" y="0" width="190" height="170" rx="4" fill="url(#silhouette-tone)"/>
      </svg>
    </section>
  </article>

  <article class="flyer flyer--back" aria-label="Flyer back">
    <p class="back__web-address">www.plumvaleforms.com.au</p>
  </article>

</body>
</html>
```